Flyer for a Business Consultant

I need a one-page description of services. I am a Brinmore Accredited Talents Mentor. I do not have a personal website but think I will soon purchase this template https://quillerlayouts.example/layouts/lectern/. I like the larger font, simplicity and larger font. I will attach his pricing flyer which I like - not to overly guide or restrict your creative thinking, but only to give a little perspective. I don't like busy, noisy - I like clarity, simplicity. Here 's the Brinmore website which these same traits https://www.brinmoretalentshub.example/ and can be a source of ideas and colors.

Target Market(s)

CEOs and Middle Managers in organizations

Industry/Entity Type

Financial Service

Colors

Designer to choose colors to be used in the design.

Requirements
Must have
• Clarity, simplicity, but also strength (not weak or frilly looking)
Nice to have
• Warm color(s), larger/not skinny font
Should not have
• Loud, noisy, busy

```html
<!DOCTYPE html>
<html lang="en">
<head>
<meta charset="utf-8">
<title>Strength-based Team Effectiveness – Services Flyer</title>
<link rel="stylesheet" href="https://fonts.googleapis.com/css2?family=Montserrat:ital,wght@1,800;1,900&family=Barlow:wght@500;600&display=swap">
<style>
  :root {
    --backdrop: #8f93ab;
    --green: #3fae3c;
    --green-light: #58c24f;
    --green-deep: #2e8f2d;
    --green-text: #4cc23e;
    --tab-dark: #12330f;
    --charcoal: #3b3b3b;
    --charcoal-top: #2c2c2c;
    --paper: #e6e6e2;
    --card: #ebebe7;
    --ink: #2d2d2d;
    --white: #ffffff;
    --logo-grey: #747474;
  }
  * { box-sizing: border-box; margin: 0; padding: 0; }
  html, body { width: 1200px; height: 1200px; overflow: hidden; }
  body { background: var(--backdrop); font-family: "Barlow", sans-serif; position: relative; }

  .flyer {
    position: absolute; left: 175px; top: 50px;
    width: 850px; height: 1100px;
    background: var(--paper);
    box-shadow: 0 6px 22px rgba(0,0,0,.25);
    overflow: hidden;
  }
  .flyer__topline { position: absolute; left: 0; top: 0; width: 100%; height: 10px; background: var(--charcoal); }

  .hero { position: absolute; left: 0; top: 10px; width: 100%; height: 322px; }
  .hero__photo {
    position: absolute; inset: 0;
    background: linear-gradient(120deg, var(--green-light) 0%, var(--green) 45%, var(--green-deep) 100%);
  }
  .hero__badge {
    position: absolute; left: 523px; top: 0; width: 308px; height: 83px;
    background: var(--white); box-shadow: 0 3px 6px rgba(0,0,0,.25);
    display: flex; align-items: center; gap: 14px; padding-left: 26px;
  }
  .badge__square { width: 53px; height: 53px; background: var(--logo-grey); flex: none; }
  .badge__name { font-family: "Barlow", sans-serif; font-weight: 500; color: var(--logo-grey); font-size: 20px; line-height: 1.15; }

  .hero__title {
    position: absolute; left: 27px; top: 164px; z-index: 2;
    font-family: "Montserrat", sans-serif; font-style: italic; font-weight: 900;
    color: var(--white); font-size: 39px; line-height: 54px; letter-spacing: -0.6px;
  }
  .hero__rule { position: absolute; left: 0; top: 274px; width: 733px; height: 2px; background: var(--white); z-index: 2; }
  .hero__lead {
    position: absolute; left: 27px; top: 283px; z-index: 2;
    font-family: "Montserrat", sans-serif; font-style: italic; font-weight: 800;
    color: var(--white); font-size: 22px; line-height: 28px;
  }

  .benefits {
    position: absolute; left: 0; top: 332px; width: 100%; height: 122px;
    background: var(--charcoal); border-top: 4px solid var(--charcoal-top);
    padding: 24px 0 0 30px; list-style: none;
  }
  .benefits li { color: var(--white); font-size: 18px; font-weight: 500; line-height: 23.5px; display: flex; gap: 10px; }
  .benefits .tick { color: var(--green-text); font-weight: 600; width: 14px; }

  .service { position: absolute; left: 29px; width: 795px; }
  .service__card {
    position: absolute; left: 0; right: 0; background: var(--card);
    box-shadow: 0 3px 5px rgba(0,0,0,.28);
    padding: 0 20px 0 27px;
  }
  .service__card p { color: var(--ink); font-size: 18px; font-weight: 500; line-height: 21.6px; white-space: nowrap; }
  .service__tab {
    position: absolute; left: 12px; top: 0; height: 44px;
    background: var(--tab-dark); display: flex; align-items: center; gap: 22px; padding-left: 18px;
    z-index: 2;
  }
  .service__tab svg { width: 20px; height: 20px; flex: none; }
  .service__tab h2 {
    font-family: "Montserrat", sans-serif; font-style: italic; font-weight: 900;
    color: var(--green-text); font-size: 24px; letter-spacing: -0.4px;
  }

  .service--individual { top: 475px; }
  .service--individual .service__tab { width: 334px; }
  .service--individual .service__card { top: 20px; height: 118px; padding-top: 38px; }

  .service--workshop { top: 637px; }
  .service--workshop .service__tab { width: 474px; }
  .service--workshop .service__card { top: 15px; height: 142px; padding-top: 36px; }

  .service--followon { top: 818px; }
  .service--followon .service__tab { width: 333px; left: 10px; }
  .service--followon .service__card { top: 16px; height: 136px; padding-top: 32px; }

  .footer__line { position: absolute; left: 0; top: 995px; width: 100%; height: 7px; background: var(--green); }
  .footer { position: absolute; left: 0; top: 1002px; width: 100%; height: 98px; background: var(--charcoal); }
  .footer__badge {
    position: absolute; left: 24px; top: 19px; width: 221px; height: 60px;
    border: 1px solid #cfcfcf; display: flex; align-items: center; gap: 11px; padding-left: 18px;
  }
  .footer__badge .badge__square { width: 38px; height: 38px; background: var(--white); }
  .footer__badge .badge__name { color: var(--white); font-size: 14.5px; }
  .footer__divider { position: absolute; left: 271px; top: 14px; width: 3px; height: 70px; background: var(--green); }
  .contact { position: absolute; left: 300px; top: 14px; list-style: none; }
  .contact li { color: var(--white); font-size: 14.5px; font-weight: 600; line-height: 16.5px; position: relative; }
  .contact svg { position: absolute; left: -19px; top: 3px; width: 11px; height: 11px; }
</style>
</head>
<body>
<main class="flyer">
  <div class="flyer__topline"></div>

  <header class="hero">
    <div class="hero__photo" role="img" aria-label="Green-tinted photo of a presenter leading a team workshop"></div>
    <div class="hero__badge">
      <span class="badge__square"></span>
      <span class="badge__name">Brinmore Accredited<br>Talents Mentor</span>
    </div>
    <h1 class="hero__title">A Strength-based Approach to<br>Managing Team Effectiveness</h1>
    <div class="hero__rule"></div>
    <p class="hero__lead">We help teams grow stronger by:</p>
  </header>

  <ul class="benefits">
    <li><span class="tick">√</span>Bringing a deep awareness of their strengths and the strengths of their associates.</li>
    <li><span class="tick">√</span>Increasing the Team’s communication and sense of partnership.</li>
    <li><span class="tick">√</span>Improving employee engagement and effectiveness.</li>
  </ul>

  <section class="service service--individual">
    <div class="service__tab">
      <svg viewBox="0 0 20 20"><polygon points="1,1 19,10 1,19" fill="#4cc23e"/></svg>
      <h2>Individual Sessions</h2>
    </div>
    <div class="service__card">
      <p>Conversational feedback and coaching sessions based on Brinmore’s TalentPrism<br>assessments. These sessions last about an hour and lead to a personalized translation of the<br>results &amp; how their strengths show up in their work and inherent blind spots they bring.</p>
    </div>
  </section>

  <section class="service service--workshop">
    <div class="service__tab">
      <svg viewBox="0 0 20 20"><polygon points="1,1 19,10 1,19" fill="#4cc23e"/></svg>
      <h2>Strength Discovery Workshop</h2>
    </div>
    <div class="service__card">
      <p>A retreat-style Team Workshop in which the team learns each other’s unique Top 5 strengths.<br>The session is very interactive and provides a common language that leads to improved<br>communication and effectiveness. Tailored in 2.3.and 4-hour options are tailored to your<br>Team’s challenges and opportunities.</p>
    </div>
  </section>

  <section class="service service--followon">
    <div class="service__tab">
      <svg viewBox="0 0 20 20"><polygon points="1,1 19,10 1,19" fill="#4cc23e"/></svg>
      <h2>Follow-on modules</h2>
    </div>
    <div class="service__card">
      <p>Follow-on is important to make the insights learned to be practical and integrated into the<br>Teams’ approach and workflows.&nbsp; In a debrief session included as part of the workshop,<br>We provide several 15-minute exercise modules for use in regular meetings, and we offer guest<br>facilitated modules of 30- 60 minutes each.</p>
    </div>
  </section>

  <div class="footer__line"></div>
  <footer class="footer">
    <div class="footer__badge">
      <span class="badge__square"></span>
      <span class="badge__name">Brinmore Accredited<br>Talents Mentor</span>
    </div>
    <div class="footer__divider"></div>
    <ul class="contact">
      <li>Corwin Ashdale</li>
      <li>Brinmore Workplace Talents Mentor</li>
      <li><svg viewBox="0 0 12 12"><rect x="0.5" y="2" width="11" height="8" fill="none" stroke="#4cc23e"/><polyline points="0.5,2 6,7 11.5,2" fill="none" stroke="#4cc23e"/></svg>corwin@talentsiq.example</li>
      <li><svg viewBox="0 0 12 12"><circle cx="6" cy="6" r="5.3" fill="none" stroke="#4cc23e"/><path d="M4 3.5 L5 5 L4.6 5.6 Q5.4 7 6.5 7.5 L7 7 L8.5 8 L8 8.8 Q5 8.6 3.4 4.2 Z" fill="#4cc23e"/></svg>555-014-2290</li>
    </ul>
  </footer>
</main>
</body>
</html>
```